Slow Harbour Airs. A CD of beautiful 17th century music for lute played by a world famous lutenist.

Hi designers,
My name is Toby Kellerman and I am an international lute player in need of a CD cover design. I am blind, so will be relying on other people's eyes and descriptions during the process, including yours! Are you up for the challenge?
My CD is called Slow Harbour Airs. It's beautiful lute music from the 17th century, very intimate and carming, but also very powerful.
I would like you to use the attached image, and find a way to include the following text in a tasteful way:
The text for the front cover is as follows:
Slow Harbour Airs
Tobias Kellerman - lute and theorbo
Music by Fenwright, Halbrook, Pilcher, Brandt, Lombretti and Ostenfeld.
Here is a cliphaven link to some of the music I play, which should give you an idea:
www.cliphaven.com/tobykellerman7
Here is a link to my website, where you can see the covers of my other CDs, and get more information about me:
www.tobiaskellerman.net
I'm excited to receive your design and ideas.
Best wishes
Toby

```html
<!DOCTYPE html>
<html lang="en">
<head>
<meta charset="utf-8">
<title>Slow Harbour Airs – Tobias Kellerman</title>
<link href="https://fonts.googleapis.com/css2?family=Quicksand:wght@300;400&display=swap" rel="stylesheet">
<style>
  :root {
    --ink-deep: #0f0b08;
    --title: #e6ae78;
    --byline: #e9c9a4;
    --credit: #dcb894;
  }
  html, body {
    margin: 0;
    padding: 0;
    width: 1200px;
    height: 1200px;
    overflow: hidden;
    background: var(--ink-deep);
  }
  .cover {
    position: relative;
    width: 1200px;
    height: 1200px;
    overflow: hidden;
    font-family: "Quicksand", sans-serif;
  }
  .metal-band {
    position: absolute;
    left: 0;
    width: 1200px;
    background:
      linear-gradient(90deg,
        #1c1510 0%, #3a2c22 8%, #7a5e4c 22%, #b8927a 30%, #5a4536 38%,
        #1a130e 50%, #2b2119 62%, #6e5443 74%, #3d2e23 86%, #2a1f17 100%);
  }
  .metal-band::after {
    content: "";
    position: absolute;
    inset: 0;
    background: linear-gradient(180deg, rgba(255,230,210,0.12), rgba(0,0,0,0.25));
  }
  .metal-band--top { top: 0; height: 86px; }
  .metal-band--bottom {
    bottom: 0;
    height: 106px;
    background:
      linear-gradient(90deg,
        #3a2c22 0%, #7a5e4c 12%, #2a1f17 22%, #5e4637 32%, #1a130e 44%,
        #3b2d23 56%, #8a6d58 70%, #b08d74 82%, #8a6b55 100%);
  }
  .performer-photo {
    position: absolute;
    top: 86px;
    left: 0;
    width: 1200px;
    height: 1008px;
    background:
      radial-gradient(ellipse 200px 380px at 380px 520px, rgba(205,170,130,0.45), rgba(0,0,0,0) 70%),
      radial-gradient(ellipse 700px 260px at 950px 860px, rgba(160,125,95,0.85), rgba(0,0,0,0) 80%),
      linear-gradient(180deg, #3a2c20 0%, #120d09 10%, #0f0b08 55%, #5a4535 72%, #8a6c52 100%);
  }
  .text-column {
    position: absolute;
    left: 683px;
    width: 480px;
    text-align: center;
    margin: 0;
  }
  .album-title {
    top: 196px;
    font-weight: 300;
    font-size: 126px;
    line-height: 150px;
    color: var(--title);
    text-shadow: 0 3px 6px rgba(0,0,0,0.6);
  }
  .album-title span { display: block; }
  .credit {
    color: var(--byline);
    font-weight: 300;
    text-shadow: 0 2px 3px rgba(0,0,0,0.6);
  }
  .credit--by { top: 730px; font-size: 38px; line-height: 48px; }
  .credit--artist { top: 826px; font-size: 50px; line-height: 60px; letter-spacing: 1px; }
  .credit--instruments { top: 900px; font-size: 28px; line-height: 36px; color: var(--credit); }
  .credit--composers {
    top: 966px;
    font-size: 21px;
    line-height: 30px;
    color: var(--credit);
    font-weight: 400;
  }
</style>
</head>
<body>
  <main class="cover">
    <div class="metal-band metal-band--top"></div>
    <div class="performer-photo" role="img" aria-label="Softly rippled photograph of the lutenist seated, playing the lute in warm low light"></div>
    <h1 class="text-column album-title"><span>Slow</span><span>Harbour</span><span>Airs</span></h1>
    <p class="text-column credit credit--by">by</p>
    <p class="text-column credit credit--artist">Tobias Kellerman</p>
    <p class="text-column credit credit--instruments">lute and theorbo</p>
    <p class="text-column credit credit--composers">Music by Fenwright, Halbrook, Pilcher,<br>Brandt, Lombretti and Ostenfeld</p>
    <div class="metal-band metal-band--bottom"></div>
  </main>
</body>
</html>
```